Store Signage for New Location

I need a banner for my new location. It needs to communicate 1: our name, 2: our phone number 3: our message. This is going to be a 7 foot wide banner that is 4 feet tall. It needs to be a very high resolution design so it prints properly.

Our phone number is (913) 548-1907

Our Message: The HONEST alternative to the dealer.

Or: Your Honest Auto Service Center

"Honest" is our key word here.

Target Market(s)

Drive-by traffic.

Industry/Entity Type

Auto Repair

Requirements
Must have
• The name of our business: Tall Pine Auto Repair
• Our phone number: (913) 548-1907
• Our message: The HONEST alternative to the dealership.
• or: Your Honest Service Center
Nice to have
• I really just need a clean layout using the uploaded logo and font. It needs to be highly visible as a sign that is seen by drive-by traffic.
• I'd like the color scheme to be the same as what I have, however, you're more than welcome to add detail and color as needed.

```html
<!DOCTYPE html>
<html lang="en">
<head>
<meta charset="utf-8">
<title>Tall Pine Auto Repair – Banner</title>
<link rel="stylesheet" href="https://fonts.googleapis.com/css2?family=Exo+2:ital,wght@0,800;1,800;1,900&display=swap">
<style>
  :root {
    --ink: #2a2a2a;
    --paper: #ffffff;
    --brand-orange: #f47b20;
    --shop-warm: #b97a6e;
    --shop-mid: #8a8f86;
    --shop-cool: #4f6274;
    --frame: #2a2a2a;
  }
  html, body {
    margin: 0;
    padding: 0;
    width: 1200px;
    height: 686px;
    overflow: hidden;
    background: var(--paper);
  }
  .banner {
    position: relative;
    width: 1200px;
    height: 686px;
    box-sizing: border-box;
    border: 2px solid var(--frame);
    background: var(--paper);
    font-family: "Exo 2", sans-serif;
    overflow: hidden;
  }
  .name-band {
    position: absolute;
    left: 0; top: 0;
    width: 100%;
    height: 228px;
    display: flex;
    align-items: center;
    border-bottom: 4px solid var(--frame);
    box-sizing: border-box;
  }
  .name-mark {
    width: 120px;
    height: 120px;
    margin-left: 58px;
    border-radius: 50%;
    background: var(--ink);
    flex: none;
  }
  .business-name {
    margin: 0 0 0 40px;
    font-weight: 800;
    font-size: 66px;
    letter-spacing: -0.5px;
    color: var(--ink);
    white-space: nowrap;
  }
  .message-band {
    position: absolute;
    left: 0; top: 228px;
    width: 100%;
    height: 326px;
  }
  .shop-photo {
    position: absolute;
    inset: 0;
    background:
      radial-gradient(ellipse at 22% 55%, rgba(214, 90, 72, 0.55), transparent 45%),
      linear-gradient(100deg, var(--shop-warm) 0%, var(--shop-mid) 45%, var(--shop-cool) 100%);
  }
  .tagline {
    position: absolute;
    right: 34px;
    top: 62px;
    margin: 0;
    text-align: right;
    font-weight: 900;
    font-style: italic;
    font-size: 94px;
    line-height: 108px;
    color: var(--paper);
    -webkit-text-stroke: 3px var(--ink);
    paint-order: stroke fill;
    text-shadow: 3px 4px 6px rgba(0, 0, 0, 0.35);
    letter-spacing: -1px;
  }
  .tagline .keyword { color: var(--brand-orange); }
  .phone-band {
    position: absolute;
    left: 0; bottom: 0;
    width: 100%;
    height: 130px;
    background: var(--brand-orange);
    border-top: 4px solid var(--frame);
    box-sizing: border-box;
    display: flex;
    align-items: center;
  }
  .phone-number {
    margin: 0 0 0 218px;
    font-weight: 800;
    font-style: italic;
    font-size: 96px;
    letter-spacing: 4px;
    color: var(--ink);
  }
</style>
</head>
<body>
  <div class="banner">
    <header class="name-band">
      <span class="name-mark" aria-hidden="true"></span>
      <h1 class="business-name">Tall Pine Auto Repair</h1>
    </header>

    <section class="message-band">
      <div class="shop-photo" role="img" aria-label="Gloved hand holding an adjustable wrench in front of a blurred auto repair shop"></div>
      <h2 class="tagline">Your <span class="keyword">Honest</span><br>Service Center</h2>
    </section>

    <footer class="phone-band">
      <p class="phone-number">(913) 548-1907</p>
    </footer>
  </div>
</body>
</html>
```